依頼詳細
A3サイズのチラシ1種類とロールバナー1種類
2つのサイズでデザインをお願いします。
(内容は全て同じで構いません)

①A3サイズ 縦297×横420mm

②ロールバナー2 縦1500mm×横910mm

------------------------------------
■入れて欲しい項目

ハルネおばさんのこぐまドーナツでは
実際に試食して納得した厳選素材のみを使用しています。

素材を生かす為に甘さを押さえた
自然な味わいをお楽しみください。

原材料のこだわり
・平飼い有精卵 → 和歌山県
・三滝製粉の小麦&全粒粉 → 北海道
・白峰バター → 北海道

味と健康へのこだわり
・毎日新品の油に100%入替
・合成着色料、人工甘味料不使用
・保存料、防腐剤不使用
・マーガリン、ショートニング不使用

各素材の詳しい内容はサイトにも記載しています。
https://harune-obasan.com/html/page3.html

※このページのデザインテイストは無視していただいて構いません。

写真はVelmora Stockの中から選んでいただければ
こちらで購入するので、プレビュー画像を入れておいて番号をお伝えください。

何か不明点があればご質問ください。
記載項目
どこかにロゴを入れておいてください。

ハルネおばさんのこぐまドーナツ!(ロゴ)
URL:https://harune-obasan.com/
サイズ
A3
ページ数
片面
希望イメージ
シンプル 複雑
単色 カラフル
暗い 明るい
日常 高級
遊び心 厳粛
未来的 伝統的
女性的 男性的
希望する色
黄・オレンジ系、茶系
納品ファイル
• イラストレーター形式 (.ai)
• PNG形式 (.png)
補足説明
添付画像(image.png)右側の
オレンジ色のロールスクリーンが実際の展示イメージです。
もう少し色々なパターンを見てみたいので締め切りを延長させていただきます。
オレンジのかわいいイメージから離れて
もう少し高級感のある感じのデザインを希望します。

ロゴももっと小さくして
ほとんど見えない程度で構いません。

高級路線の別商品もあるので
これに同じように高級感と
素材の安心感が全面に伝わるものが希望です。

https://tori-kintsubaya.com/

別商品の画像も添付しておきますので
参考にしてみてください。

もう少しデザイン案を見てみたいので
少し締切日を延長させていただきます。
■ 選んだ理由

可愛らしさと高級感のバランスが絶妙で、インパクトがあって目立つという点でもこちらの希望通りのデザインだったので選ばせていただきました。

■ 提案者全員のお礼・コメント

たくさんのご提案ありがとうございました。また機会があればぜひ宜しくお願いします。

```html
<!DOCTYPE html>
<html lang="ja">
<head>
<meta charset="UTF-8">
<title>ハルネおばさんのこぐまドーナツ</title>
<link rel="stylesheet" href="https://fonts.googleapis.com/css2?family=M+PLUS+Rounded+1c:wght@500;700;800;900&family=Noto+Sans+JP:wght@400;700&family=Noto+Serif+JP:wght@600&display=swap">
<style>
:root{
  --orange:#f5a524;
  --orange-light:#fbc85a;
  --orange-deep:#ef8a12;
  --title-pink:#e6405f;
  --brown:#5b3420;
  --brown-soft:#8a5a36;
  --cream:#fffaf0;
  --white:#ffffff;
}
*{margin:0;padding:0;box-sizing:border-box}
html,body{width:853px;height:1200px;overflow:hidden;background:var(--orange)}
.flyer{
  position:relative;width:853px;height:1200px;overflow:hidden;
  background:radial-gradient(circle at 50% 40%,var(--orange-light) 0%,var(--orange) 55%,var(--orange-deep) 100%);
  font-family:"Noto Sans JP",sans-serif;color:var(--brown);
}
.bubble{
  position:absolute;border-radius:50%;background:var(--white);
  display:flex;flex-direction:column;align-items:center;justify-content:center;text-align:center;
  box-shadow:0 4px 10px rgba(120,60,0,.18);
}
.bubble--select{left:30px;top:8px;width:290px;height:290px;padding:0 40px}
.bubble--natural{left:600px;top:486px;width:230px;height:230px;padding:0 22px}
.bubble__head{font-family:"M PLUS Rounded 1c",sans-serif;font-weight:900;color:var(--orange-deep);line-height:1.15;white-space:nowrap}
.bubble--select .bubble__head{font-size:40px;margin-bottom:8px}
.bubble--select .bubble__head small{font-size:26px}
.bubble--natural .bubble__head{font-size:28px;margin-bottom:8px;color:var(--brown-soft)}
.bubble__body{font-size:17px;line-height:1.5;font-weight:700;color:var(--brown)}
.bubble--natural .bubble__body{font-size:15px}
.photo-circle{position:absolute;border-radius:50%;border:6px solid var(--white);box-shadow:0 4px 10px rgba(120,60,0,.2)}
.photo-circle--top{left:640px;top:10px;width:190px;height:190px;background:radial-gradient(circle at 45% 45%,#f6d2b2,#c9865a 75%,#7b4a2e)}
.photo-circle--left{left:30px;top:500px;width:180px;height:180px;background:radial-gradient(circle at 50% 45%,#f7dcc4,#d59d78 70%,#9b6a4b)}
.brand-mark{position:absolute;left:350px;top:196px;display:flex;align-items:center;gap:12px}
.brand-mark__dot{width:34px;height:34px;border-radius:50%;background:var(--brown)}
.brand-mark__name{font-family:"M PLUS Rounded 1c",sans-serif;font-weight:800;font-size:30px;color:var(--brown);line-height:1}
.title{
  position:absolute;left:0;right:0;top:300px;text-align:center;
  font-family:"M PLUS Rounded 1c",sans-serif;font-weight:900;font-size:78px;line-height:92px;
  color:var(--title-pink);letter-spacing:2px;white-space:nowrap;
  -webkit-text-stroke:10px var(--white);paint-order:stroke fill;
  text-shadow:0 5px 0 var(--brown);
}
.panel{
  position:absolute;left:28px;top:725px;width:797px;height:475px;
  background:var(--cream);border-radius:18px 18px 0 0;padding:14px 26px 0;
}
.panel__heading{
  text-align:center;font-family:"M PLUS Rounded 1c",sans-serif;font-weight:800;font-size:30px;line-height:40px;color:var(--brown);
  display:flex;align-items:center;justify-content:center;gap:16px;
}
.panel__heading::before,.panel__heading::after{content:"";width:90px;height:3px;background:var(--orange)}
.ingredients{display:flex;justify-content:space-between;margin-top:10px}
.ingredient{width:240px}
.ingredient__name{font-family:"Noto Serif JP",serif;font-weight:600;font-size:17px;line-height:24px;text-align:center;margin-bottom:6px;color:var(--brown);white-space:nowrap}
.ingredient__photo{position:relative;height:165px;border-radius:4px}
.ingredient__photo--butter{background:linear-gradient(135deg,#fff3c4,#f0d58a 60%,#d9b86a)}
.ingredient__photo--flour{background:linear-gradient(135deg,#eee4d4,#c9b59a 60%,#9e8668)}
.ingredient__photo--egg{background:linear-gradient(135deg,#c98856,#a0582c 55%,#6e3a1c)}
.ingredient__origin{position:absolute;right:10px;bottom:8px;color:var(--white);font-weight:700;font-size:16px;text-shadow:0 1px 3px rgba(0,0,0,.5)}
.panel__heading--health{margin-top:16px}
.promises{display:flex;justify-content:center;gap:48px;margin-top:10px;list-style:none}
.promise{
  width:130px;height:130px;border-radius:50%;background:var(--orange);
  display:flex;align-items:center;justify-content:center;text-align:center;
  color:var(--white);font-weight:700;font-size:14px;line-height:1.45;padding:0 6px;white-space:nowrap;
}
</style>
</head>
<body>
<main class="flyer">
  <div class="bubble bubble--select">
    <p class="bubble__head">厳選素材<br><small>のみを使用</small></p>
    <p class="bubble__body">ハルネおばさんのこぐまドーナツは実際に試食して納得した厳選素材のみを使用しています。</p>
  </div>
  <div class="photo-circle photo-circle--top" role="img" aria-label="ドーナツを手に笑う子どもの写真"></div>

  <div class="brand-mark">
    <span class="brand-mark__dot"></span>
    <span class="brand-mark__name">harune homemade</span>
  </div>

  <h1 class="title">ハルネおばさんの<br>こぐまドーナツ</h1>

  <div class="photo-circle photo-circle--left" role="img" aria-label="ドーナツを食べる子どもの写真"></div>

  <div class="bubble bubble--natural">
    <p class="bubble__head">自然な味わい</p>
    <p class="bubble__body">素材を生かす為に甘さを押さえた自然な味わいをお楽しみください。</p>
  </div>

  <section class="panel">
    <h2 class="panel__heading">原材料のこだわり</h2>
    <div class="ingredients">
      <figure class="ingredient">
        <figcaption class="ingredient__name">白峰バター</figcaption>
        <div class="ingredient__photo ingredient__photo--butter" role="img" aria-label="バターの写真"><span class="ingredient__origin">北海道</span></div>
      </figure>
      <figure class="ingredient">
        <figcaption class="ingredient__name">三滝製粉の小麦&amp;全粒粉</figcaption>
        <div class="ingredient__photo ingredient__photo--flour" role="img" aria-label="小麦粉の写真"><span class="ingredient__origin">北海道</span></div>
      </figure>
      <figure class="ingredient">
        <figcaption class="ingredient__name">平飼い有精卵</figcaption>
        <div class="ingredient__photo ingredient__photo--egg" role="img" aria-label="卵の写真"><span class="ingredient__origin">和歌山県</span></div>
      </figure>
    </div>

    <h2 class="panel__heading panel__heading--health">味と健康へのこだわり</h2>
    <ul class="promises">
      <li class="promise">毎日新品の油に<br>100%入替</li>
      <li class="promise">合成着色料<br>人工甘味料<br>不使用</li>
      <li class="promise">保存料、防腐剤<br>不使用</li>
      <li class="promise">マーガリン<br>ショートニング<br>不使用</li>
    </ul>
  </section>
</main>
</body>
</html>
```